Bref créative
Corwin T. Halbeck D.D.S.
Family Dentistry
Professional
438 W. FM 2296
Suite - B
Crowley, TX 76052
corwinthalbeckdds@mailvexo.com
I would like the logo to be designed into this as well as the name of the practice. Which is "Corwin T. Halbeck D.D.S."
This is the side where we write when the patient has a future appointment. usually a space is given to write the date. Followed by a list of the days of the week to indicate that as well as the time of the appointment.
Also incorporate If you must cancel your appointment with us please do so at least 48 hours in advance. Thank you
Please use these logos to design stationary and cards. I like the brushed stroked star for printed materials. The solid version is more for monogramming.

```html
<!DOCTYPE html>
<html lang="en">
<head>
<meta charset="utf-8">
<title>Corwin T. Halbeck D.D.S. — Stationery</title>
<link href="https://fonts.googleapis.com/css2?family=Cinzel:wght@400;600&family=Lato:wght@400;700&display=swap" rel="stylesheet">
<style>
:root{
  --bg:#ece6de;
  --paper:#ffffff;
  --brown:#6e3d2c;
  --brown-dark:#57301f;
  --slate:#4b4f52;
  --ink:#4a3a33;
  --muted:#9a8f88;
  --rule:#d8cfc7;
  --faint:#efe9e4;
}
*{box-sizing:border-box;margin:0;padding:0}
html,body{width:1200px;height:382px;overflow:hidden;background:var(--bg)}
body{position:relative;font-family:"Lato",sans-serif;color:var(--ink)}
.piece{position:absolute}
.paper{background:var(--paper);box-shadow:0 1px 3px rgba(0,0,0,.18)}
.label{position:absolute;font-size:6px;color:var(--muted);letter-spacing:.3px;white-space:nowrap}

/* title block */
.title-block{left:40px;top:20px;width:240px}
.title-block .name{font-family:"Cinzel",serif;font-size:21px;color:var(--brown);letter-spacing:.5px;line-height:1}
.title-block .tagline{font-family:"Cinzel",serif;font-size:7px;letter-spacing:4px;color:var(--muted);margin-top:4px;text-transform:uppercase}
.title-block .proposal{font-size:6.5px;color:var(--muted);margin-top:10px}

/* wordmark */
.wordmark{display:flex;align-items:center;gap:4px;font-family:"Cinzel",serif;color:var(--brown);white-space:nowrap}
.wordmark .dot{display:inline-block;border-radius:50%;background:var(--brown)}
.wordmark.light{color:#fff}
.wordmark.light .dot{background:#fff}
.subline{font-family:"Cinzel",serif;text-transform:uppercase;color:var(--muted);letter-spacing:2px}

/* appointment cards */
.card{width:120px;height:70px;padding:7px 8px}
.card h4{font-size:6px;font-weight:700;letter-spacing:.5px;margin-bottom:4px;text-align:center}
.line{display:flex;align-items:flex-end;gap:3px;font-size:5px;margin-bottom:4px}
.line span.fill{flex:1;border-bottom:.6px solid currentColor;opacity:.6;height:5px}
.days{display:flex;justify-content:space-between;font-size:4.6px;margin:3px 0}
.days span{border:.5px solid currentColor;padding:1px 2px;border-radius:1px}
.note{font-size:4.2px;line-height:1.35;text-align:center;opacity:.85}

.appt-front{left:19px;top:144px;border:1px solid var(--rule)}
.appt-back{left:19px;top:254px;background:var(--brown);color:#f4ebe5}
.appt-back h4{color:#fff}

.biz{width:120px;height:68px;padding:8px}
.biz-front{left:149px;top:163px}
.biz-back{left:149px;top:283px;display:flex;flex-direction:column;justify-content:center;align-items:center;gap:3px}
.biz .contact{font-size:4.6px;line-height:1.5;margin-top:6px;color:var(--ink)}
.biz .band{position:absolute;left:0;bottom:0;width:100%;height:5px;background:var(--brown)}

/* letterheads */
.letterhead{width:247px;height:331px;top:24px;padding:16px 18px}
.lh-one{left:293px}
.lh-two{left:569px}
.lh-head{display:flex;justify-content:space-between;align-items:flex-start;border-bottom:.6px solid var(--rule);padding-bottom:6px}
.lh-head .contact{font-size:4.3px;line-height:1.5;text-align:right;color:var(--muted)}
.lh-watermark{position:absolute;left:0;right:0;top:120px;text-align:center;font-family:"Cinzel",serif;font-size:22px;color:var(--faint);letter-spacing:1px;line-height:1.2}
.lh-foot{position:absolute;left:18px;right:18px;bottom:12px;border-top:.6px solid var(--rule);padding-top:4px;font-size:4.3px;color:var(--muted);text-align:center}
.lh-side{position:absolute;top:0;bottom:0;width:6px;background:var(--brown)}
.lh-one .lh-side{left:0}
.lh-two .lh-side{right:0;background:var(--slate)}

/* envelopes */
.envelope{width:324px;height:110px;left:852px;overflow:hidden}
.envelope svg{position:absolute;left:0;top:0}
.env-slate{top:24px;background:var(--slate)}
.env-brown{top:122px;background:var(--brown)}
.env-white{top:220px;background:var(--paper)}
.envelope .wordmark{position:absolute;left:12px;bottom:12px;font-size:7px}
.env-white .wordmark{bottom:14px}
</style>
</head>
<body>

<header class="piece title-block">
  <div class="name">Corwin T. Halbeck D.D.S.</div>
  <div class="tagline">Family Dentistry</div>
  <div class="proposal">Stationery Proposal</div>
</header>

<!-- appointment card front -->
<section class="piece paper card appt-front">
  <h4 style="color:var(--brown)">Next Appointment</h4>
  <div class="line">Patient <span class="fill"></span></div>
  <div class="line">Date <span class="fill"></span></div>
  <div class="days"><span>Mon</span><span>Tue</span><span>Wed</span><span>Thu</span><span>Fri</span><span>Sat</span></div>
  <div class="line">Time <span class="fill"></span> AM / PM</div>
  <p class="note">If you must cancel your appointment with us please do so at least 48 hours in advance. Thank you</p>
</section>
<span class="label" style="left:19px;top:218px">Appointment Card Front</span>

<!-- business card front -->
<section class="piece paper biz biz-front">
  <div class="wordmark" style="font-size:7px"><span class="dot" style="width:6px;height:6px"></span>Corwin T. Halbeck D.D.S.</div>
  <div class="subline" style="font-size:3.8px;margin:2px 0 0 10px">Family Dentistry</div>
  <div class="contact">438 W. FM 2296, Suite - B<br>Crowley, TX 76052<br>(817) 555-0142<br>corwinthalbeckdds@mailvexo.com</div>
  <div class="band"></div>
</section>
<span class="label" style="left:149px;top:235px">Business Card Front</span>

<!-- appointment card back -->
<section class="piece card appt-back">
  <h4>Your Appointment</h4>
  <div class="line">On <span class="fill"></span></div>
  <div class="days"><span>Mon</span><span>Tue</span><span>Wed</span><span>Thu</span><span>Fri</span><span>Sat</span></div>
  <div class="line">At <span class="fill"></span> AM / PM</div>
  <p class="note">If you must cancel your appointment with us please do so at least 48 hours in advance. Thank you</p>
</section>
<span class="label" style="left:19px;top:328px">Appointment Card Back</span>

<!-- business card back -->
<section class="piece paper biz biz-back">
  <div class="wordmark" style="font-size:8px"><span class="dot" style="width:7px;height:7px"></span>Corwin T. Halbeck D.D.S.</div>
  <div class="subline" style="font-size:4px">Family Dentistry</div>
</section>
<span class="label" style="left:149px;top:355px">Business Card Back</span>

<!-- letterhead one -->
<section class="piece paper letterhead lh-one">
  <div class="lh-side"></div>
  <div class="lh-head">
    <div>
      <div class="wordmark" style="font-size:8px"><span class="dot" style="width:7px;height:7px"></span>Corwin T. Halbeck D.D.S.</div>
      <div class="subline" style="font-size:4px;margin:2px 0 0 11px">Family Dentistry</div>
    </div>
    <div class="contact">438 W. FM 2296, Suite - B<br>Crowley, TX 76052<br>(817) 555-0142<br>corwinthalbeckdds@mailvexo.com</div>
  </div>
  <div class="lh-watermark">Corwin T.<br>Halbeck D.D.S.</div>
</section>
<span class="label" style="left:380px;top:362px">Letterhead</span>

<!-- letterhead two -->
<section class="piece paper letterhead lh-two">
  <div class="lh-side"></div>
  <div class="lh-head" style="border:none">
    <div>
      <div class="wordmark" style="font-size:8px"><span class="dot" style="width:7px;height:7px"></span>Corwin T. Halbeck D.D.S.</div>
      <div class="subline" style="font-size:4px;margin:2px 0 0 11px">Family Dentistry</div>
    </div>
  </div>
  <div class="lh-watermark">Corwin T.<br>Halbeck D.D.S.</div>
  <div class="lh-foot">438 W. FM 2296, Suite - B · Crowley, TX 76052 · (817) 555-0142 · corwinthalbeckdds@mailvexo.com</div>
</section>
<span class="label" style="left:648px;top:362px">Letterhead Alternate</span>

<!-- envelopes -->
<section class="piece envelope env-slate">
  <svg width="324" height="110" viewBox="0 0 324 110"><polyline points="0,0 162,58 324,0" fill="none" stroke="rgba(255,255,255,.25)" stroke-width="1"/></svg>
  <div class="wordmark light"><span class="dot" style="width:6px;height:6px"></span>Corwin T. Halbeck D.D.S.</div>
</section>
<section class="piece envelope env-brown">
  <svg width="324" height="110" viewBox="0 0 324 110"><polyline points="0,0 162,58 324,0" fill="none" stroke="rgba(255,255,255,.25)" stroke-width="1"/></svg>
  <div class="wordmark light"><span class="dot" style="width:6px;height:6px"></span>Corwin T. Halbeck D.D.S.</div>
</section>
<section class="piece paper envelope env-white">
  <svg width="324" height="110" viewBox="0 0 324 110"><polyline points="0,0 162,58 324,0" fill="none" stroke="var(--rule)" stroke-width="1"/></svg>
  <div class="wordmark"><span class="dot" style="width:6px;height:6px"></span>Corwin T. Halbeck D.D.S.</div>
</section>
<span class="label" style="left:1000px;top:340px">Envelopes</span>

</body>
</html>
```